Re jig a A4 Instructional Flyer

We need an established A4 instructional Flyer (2 pages x A4) - to be rejigged in Harlow Academy of Learning Branding to look fresh and new.

Permissions have been received to rejig this Medical Triage Chart. Fresh branding and setting out (fonts) required.

FOOTER NOTES : to be inserted at the bottom of the A4 instruction sheet

Harlow Academy produced with permissions from Coastal Care Alliance, produced by Coastal Care Alliance with Clinic Circle Eastgate with permissions from Southern Basin Careline Hub. Harlow acknowledges the FMPCB Standards Criterion 3.2.3 Practice Training and Education in Triage

Target Market(s)

Medical Practices

Industry/Entity Type

Health

Font styles to use
Serif

Colors
0255a3
f78f20

Requirements
Must have
• Professional
• Pops of colour in the chart.
• This chart is to be USED and is VISUAL (no boring grey words throughout)
• PROBS SANS SERIF but SERIF for titles OK
Nice to have
• look at www.harlowlearning.edu.au FOR BRANDING look and feel

```html
<!DOCTYPE html>
<html lang="en">
<head>
<meta charset="utf-8">
<title>Front Desk Triage – Harlow Academy of Learning</title>
<link rel="stylesheet" href="https://fonts.googleapis.com/css2?family=Roboto:ital,wght@0,300;0,400;0,700;0,900;1,300;1,700&display=swap">
<style>
  :root{
    --brand-blue:#0255a3;
    --brand-orange:#f78f20;
    --ink:#1a1a1a;
    --white:#ffffff;
    --paper:#ffffff;
  }
  *{box-sizing:border-box;margin:0;padding:0}
  html,body{width:1200px;height:848px;overflow:hidden;background:var(--paper)}
  body{font-family:"Roboto",Arial,sans-serif;color:var(--ink);position:relative}
  .sheet{position:relative;width:1200px;height:848px}

  .brand{position:absolute;left:46px;top:48px;width:150px;display:flex;flex-direction:column;align-items:center;gap:10px}
  .brand-mark{width:44px;height:44px;border-radius:50%;background:var(--brand-blue)}
  .brand-name{font-family:"Roboto",Arial,sans-serif;font-weight:700;font-size:15px;line-height:1.2;color:var(--brand-blue);text-align:center;text-transform:uppercase;letter-spacing:.5px}

  .title{position:absolute;left:220px;top:34px}
  .title-main{font-weight:900;font-size:41px;color:var(--brand-blue);letter-spacing:-.5px;line-height:1.1}
  .title-sub{font-weight:700;font-size:37px;color:var(--brand-orange);line-height:1.18;margin-top:4px;width:860px}

  .col{position:absolute;top:192px;font-size:12.8px;line-height:16.8px;font-weight:300}
  .col-left{left:45px;width:358px}
  .col-mid{left:425px;width:350px}
  .divider{position:absolute;left:409px;top:193px;height:565px;border-left:1.5px dashed var(--brand-blue)}

  h2{font-weight:700;font-size:18px;line-height:22px;color:var(--brand-orange);text-transform:uppercase;margin-bottom:3px;letter-spacing:-.2px}
  .bullets{list-style:none}
  .bullets li{position:relative;padding-left:13px;margin-bottom:7px}
  .bullets li::before{content:"•";position:absolute;left:2px;top:0}
  .steps{list-style:none;margin-bottom:0}
  .steps li{padding-left:13px;text-indent:-13px;margin-bottom:2.5px}
  .steps b,.cat b{color:var(--brand-blue);font-weight:700}
  .section{margin-bottom:16px}

  .cat{list-style:none}
  .cat li{position:relative;padding-left:10px;margin-bottom:9.5px}
  .cat li::before{content:"•";position:absolute;left:0;color:var(--brand-blue);font-weight:700}

  .action-plan{position:absolute;left:45px;top:622px;width:366px;height:135px;background:var(--brand-blue);color:var(--white);padding:9px 13px;font-size:12.8px;line-height:16.8px;font-weight:300}
  .action-plan h3{color:var(--brand-orange);font-size:14.5px;font-weight:700;margin-bottom:3px}
  .action-plan .call{margin-top:9px;font-weight:700;font-size:14.5px}
  .action-plan .call span{color:var(--brand-orange)}

  .scheduling{position:absolute;left:787px;top:193px;width:380px;height:565px;background:var(--brand-blue);color:var(--white);padding:20px 18px 0 19px;font-size:12.8px;line-height:16.8px;font-weight:300}
  .scheduling h2{margin-bottom:6px}
  .scheduling .bullets li{padding-left:10px;margin-bottom:5px}
  .scheduling .bullets li::before{color:var(--brand-orange);left:0}
  .scheduling strong{color:var(--brand-orange);font-weight:700}
  .record-note{position:absolute;left:19px;top:460px;width:350px;color:var(--brand-orange);font-weight:700;font-style:italic;font-size:13.2px;line-height:17px}

  .footer{position:absolute;left:0;top:779px;width:1200px;text-align:center;color:var(--brand-blue);font-size:12.8px;line-height:17.5px;font-weight:300}
</style>
</head>
<body>
<main class="sheet">
  <div class="brand">
    <div class="brand-mark"></div>
    <div class="brand-name">Harlow Academy<br>of Learning</div>
  </div>

  <header class="title">
    <h1 class="title-main">FRONT DESK TRIAGE</h1>
    <p class="title-sub">How to manage common scenarios faced by reception staff</p>
  </header>

  <section class="col col-left">
    <div class="section">
      <h2>Is this an emergency?</h2>
      <ul class="bullets">
        <li>When answering the telephone, all callers should be asked if the matter is an emergency prior to being placed on hold: Ask the patient, <i>“Is this an emergency or can I place you on hold for a moment?”</i></li>
        <li>Consider the TRIAGE STEPS and CATEGORIES listed on the reverse of this document to assess the patient’s status.</li>
      </ul>
    </div>
    <div class="section">
      <h2>Ask the patient – Triage steps</h2>
      <ol class="steps">
        <li><b>1.</b> Confirm the patient’s name and phone number.</li>
        <li><b>2.</b> Does the patient attend the surgery? (ie Does the practice have previous medical records to hand?)</li>
        <li><b>3.</b> Location. <i>(“Are you at home?” “Are you alone?”)</i></li>
        <li><b>4.</b> Nature of their problem. (Patient may prefer to speak to the practice nurse or on call doctor.)</li>
        <li><b>5.</b> Duration of their symptoms. <i>(“How long have you felt like this?”)</i></li>
        <li><b>6.</b> Severity of their problem. <i>(“On a scale of 1 to 10 how severe is the pain?”</i> [if applicable].)</li>
        <li><b>7.</b> Any previous major health problems. <i>(“Are you on any medication?” “Do you have any allergies?”)</i></li>
      </ol>
    </div>
  </section>

  <div class="divider"></div>

  <section class="col col-mid">
    <div class="section">
      <h2>On the day emergencies in<br>the clinic</h2>
      <ul class="cat">
        <li><b>Category 1</b> patients should immediately be seen by the on-call doctor or other medical professional on duty.</li>
        <li><b>Category 2</b> patients should be directed to the emergency department of their nearest hospital.</li>
        <li><b>Category 3</b> patients or patients with worsening symptoms should be referred to the practice nurse or on call doctor.</li>
        <li><b>Category 4</b> patients should be advised to attend the clinic immediately and triaged by the practice nurse (may then be slotted in between appointments or at the end of the session).</li>
        <li><b>Category 5</b> patients should make an appointment for the day and be advised to call back if symptoms worsen.</li>
        <li><b>Category 6</b> patients should make an appointment within 24 hours and call back if symptoms worsen.</li>
      </ul>
    </div>
    <div class="section">
      <h2>Patients presenting with symptoms of potential communicable diseases</h2>
      <ul class="bullets">
        <li>Such as ‘influenza’(‘flu), measles, chicken pox should be isolated to a secluded area of the medical practice such as the nurses’ office. Where possible, a notice of isolation is to be fixed to the door to limit access in this area.</li>
        <li>Patients with ‘flu like symptoms should be required to wear a surgical mask.</li>
        <li>If the patient is bleeding or vomiting, put gloves on before you assist them.</li>
      </ul>
    </div>
  </section>

  <aside class="action-plan">
    <h3>EMERGENCY ACTION PLAN</h3>
    <div>• Remain calm and don not panic.</div>
    <div>• Be aware and respond to the needs of the emergency.</div>
    <div>• Assess which patient needs to take priority.</div>
    <div>• Deal with any injury or illness in order of severity.</div>
    <p class="call"><span>CALL 000</span> FOR AMBULANCE, POLICE OR FIRE</p>
  </aside>

  <aside class="scheduling">
    <h2>Scheduling care</h2>
    <ul class="bullets">
      <li>Reception staff should reserve several unbooked appointment times each day for ‘on the day’ urgent appointments such as unwell children and the elderly, lacerations and suspected fractures.</li>
      <li>If your practice does not operate on an appointment system, patients should be triaged on walk in and advised of the expected waiting time to see the doctor, nurse or Aboriginal health worker.</li>
      <li>Where a patient is assessed as in need of urgent medical attention over the telephone, advise the caller to hang up and call <strong>000</strong> immediately for an ambulance.</li>
      <li>Where a receptionist is unable to determine the urgency of a telephone call, the patient should be transferred to the practice nurse or on-call doctor for triage.</li>
      <li>If a patient presents in person and requires urgent medical assistance after the doctor has left – call <strong>000</strong> for ambulance.</li>
      <li>Clinical staff treating the patient should wear as a minimum, a surgical mask, gloves and when collecting nose and/or throat swabs, protective eyewear.</li>
    </ul>
    <p class="record-note">All emergency cases dealt with by reception should be recorded by the staff member involved in the patient health record in addition to the clinical notes recorded by the practice nurse or doctor/s treating the patient.</p>
  </aside>

  <footer class="footer">
    Harlow Academy produced with permissions from Coastal Care Alliance, produced by Coastal Care Alliance with Clinic Circle Eastgate with permissions from Southern Basin Careline Hub.<br>
    Harlow acknowledges the FMPCB Standards Criterion 3.2.3 Practice Training and Education in Triage
  </footer>
</main>
</body>
</html>
```